Rack Card for Roving Glow Crew

Please read this thoroughly and double-check these requirements before submitting any design. A single design submission will include both the front and the back. Do not submit the front and the back separately. Do not submit multiple designs that look similar. I have attached content and pictures. The rack cards are 3.74" inches wide by 8.27" inches high. There must be room for bleed / cut-off. It is highly recommended that you test your image or PDF design on the plume press website before submitting.

Target Market(s)

see attached.

Industry/Entity Type

see attached.

Requirements
Must have
• see attached.
Nice to have
• see attached.
Should not have
• see attached.

```html
<!DOCTYPE html>
<html lang="en">
<head>
<meta charset="utf-8">
<title>Roving Glow Crew – Rack Card</title>
<link href="https://fonts.googleapis.com/css2?family=Playball&family=DM+Serif+Display&family=Poppins:wght@400;500;600;700&display=swap" rel="stylesheet">
<style>
  :root {
    --teal-dark: #1d5a54;
    --teal-script: #79b3aa;
    --teal-light: #8fd3cd;
    --teal-panel: #d3ecec;
    --white: #ffffff;
    --stage: #b4b4b4;
  }
  * { margin: 0; padding: 0; box-sizing: border-box; }
  html, body { width: 1200px; height: 1117px; overflow: hidden; }
  body { background: var(--stage); font-family: 'Poppins', sans-serif; position: relative; }

  .rack-card { position: absolute; top: 63px; width: 439px; height: 972px; background: var(--white); overflow: hidden; }
  .rack-card--front { left: 134px; }
  .rack-card--back { left: 600px; }
  .abs { position: absolute; }

  /* Front */
  .hero-photo { left: 0; top: 0; width: 439px; height: 400px; background: linear-gradient(150deg, #a58c78 0%, #e8ddd3 40%, #f3efe9 60%, #cbbfb2 100%); }
  .hero-curve { left: 0; top: 300px; width: 439px; height: 110px; }
  .headline-script { left: 0; width: 439px; top: 356px; text-align: center; font-family: 'Playball', cursive; font-size: 86px; line-height: 1; color: var(--teal-script); white-space: nowrap; }
  .headline-sub { left: 56px; width: 327px; top: 441px; display: flex; align-items: center; gap: 12px; font-family: 'DM Serif Display', serif; font-size: 30px; color: var(--teal-dark); line-height: 1; }
  .headline-sub::before, .headline-sub::after { content: ""; flex: 1; height: 1.5px; background: var(--teal-dark); }
  .headline-main { left: 0; width: 439px; top: 469px; text-align: center; font-family: 'DM Serif Display', serif; font-size: 61px; line-height: 1; color: var(--teal-dark); white-space: nowrap; }
  .intro { left: 20px; width: 399px; top: 545px; text-align: center; font-weight: 600; font-size: 13.6px; line-height: 18px; color: var(--teal-dark); white-space: nowrap; }

  .services-panel { left: 0; top: 608px; width: 439px; height: 226px; background: var(--teal-panel); }
  .services-rule { left: 41px; top: 625px; width: 357px; height: 12px; }
  .services-label { left: 168px; top: 620px; width: 103px; height: 21px; text-align: center; color: var(--white); font-weight: 600; font-size: 13px; line-height: 21px; letter-spacing: .3px; }
  .service-item { display: flex; gap: 10px; font-weight: 600; font-size: 12.3px; line-height: 15px; color: var(--teal-dark); white-space: nowrap; }
  .service-item svg { flex: none; margin-top: 2px; }

  .gallery-frame { left: 18px; top: 740px; width: 404px; height: 184px; background: var(--white); border-radius: 12px; box-shadow: 0 4px 8px rgba(0,0,0,.12); }
  .gallery { left: 21px; top: 743px; width: 398px; height: 178px; border-radius: 10px; overflow: hidden; display: flex; }
  .gallery > div { flex: 1; }
  .g1 { background: linear-gradient(160deg, #e7e2dc, #d8c9aa 55%, #efe9e2); }
  .g2 { background: linear-gradient(160deg, #dedbd6, #d9c08f 55%, #ece6dc); }
  .g3 { background: linear-gradient(160deg, #f0ece8, #dccbb2 50%, #ebdbd6); }

  .url-bar { left: 86px; top: 925px; width: 266px; height: 47px; background: linear-gradient(90deg, var(--teal-dark), #4f8f88 50%, var(--teal-dark)); color: var(--white); font-weight: 600; font-size: 13.5px; text-align: center; line-height: 44px; }

  /* Back */
  .portrait-photo { left: 0; top: 0; width: 439px; height: 420px; background: linear-gradient(135deg, #2a2622 0%, #6b4a3c 35%, #d6a48c 60%, #3a2f2c 100%); }
  .back-curve { left: 0; top: 350px; width: 439px; height: 80px; }
  .back-band { left: 0; top: 420px; width: 439px; height: 243px; background: var(--teal-dark); }
  .back-lead { left: 10px; width: 419px; top: 446px; text-align: center; color: var(--white); font-weight: 600; font-size: 13.6px; line-height: 19.8px; white-space: nowrap; }
  .duo-frame { top: 521px; width: 202px; height: 134px; background: var(--white); border-radius: 12px; padding: 4px; }
  .duo-frame > div { width: 100%; height: 100%; border-radius: 9px; }
  .duo-a { left: 16px; } .duo-a > div { background: linear-gradient(150deg, #4a3a30, #b59072 50%, #e6ddd6); }
  .duo-b { left: 221px; } .duo-b > div { background: linear-gradient(150deg, #c8b6a6, #5a4233 50%, #e2d6cc); }

  .onsite-note { left: 35px; top: 671px; width: 180px; font-size: 11.6px; line-height: 14.7px; color: var(--teal-dark); white-space: nowrap; }
  .include-label { left: 238px; top: 669px; font-weight: 700; font-size: 11.8px; color: var(--teal-dark); }
  .include-row { left: 226px; width: 213px; height: 20px; background: var(--teal-panel); display: flex; align-items: center; gap: 9px; padding-left: 12px; font-weight: 600; font-size: 12.2px; color: var(--teal-dark); }

  .fees-box { left: 17px; top: 803px; width: 403px; height: 112px; border: 1.5px solid var(--teal-dark); border-radius: 10px; background: var(--white); box-shadow: 0 4px 0 var(--teal-panel); padding: 10px 16px; color: var(--teal-dark); }
  .fees-title { font-weight: 600; font-size: 12px; margin-bottom: 4px; }
  .fee-item { display: flex; gap: 12px; font-size: 11px; line-height: 13.5px; margin-bottom: 5px; }
  .fee-item svg { flex: none; margin-top: 1px; }

  .back-footer { left: 0; top: 932px; width: 439px; height: 40px; background: linear-gradient(90deg, var(--teal-dark), #5c9891 50%, var(--teal-dark)); color: var(--white); font-weight: 600; font-size: 14px; text-align: center; line-height: 40px; }
</style>
</head>
<body>

<svg width="0" height="0" style="position:absolute">
  <defs>
    <symbol id="tick-soft" viewBox="0 0 12 12"><circle cx="6" cy="6" r="6" fill="#79b3aa"/><path d="M3.3 6.2l1.8 1.8 3.6-3.7" stroke="#fff" stroke-width="1.5" fill="none"/></symbol>
    <symbol id="tick-dark" viewBox="0 0 12 12"><circle cx="6" cy="6" r="6" fill="#1d5a54"/><path d="M3.3 6.2l1.8 1.8 3.6-3.7" stroke="#fff" stroke-width="1.5" fill="none"/></symbol>
  </defs>
</svg>

<section class="rack-card rack-card--front">
  <div class="abs hero-photo" role="img" aria-label="Photo of a bride with a pearl-pinned updo having her makeup applied"></div>
  <svg class="abs hero-curve" viewBox="0 0 439 110">
    <path d="M0,63 Q219.5,-1 439,63 V110 H0 Z" fill="#8fd3cd"/>
    <path d="M0,83 Q219.5,-11 439,83" stroke="#1d5a54" stroke-width="3" fill="none"/>
    <path d="M0,87 Q219.5,-11 439,87 V110 H0 Z" fill="#fff"/>
  </svg>
  <div class="abs headline-script">We travel</div>
  <div class="abs headline-sub">to you on your</div>
  <div class="abs headline-main">special day!</div>
  <p class="abs intro">We provide you with professional<br>makeup artists and hairstylist that will travel<br>to your location.</p>

  <div class="abs services-panel"></div>
  <svg class="abs services-rule" viewBox="0 0 357 12">
    <line x1="0" y1="4" x2="357" y2="4" stroke="#1d5a54" stroke-width="1.5"/>
    <line x1="0" y1="8" x2="357" y2="8" stroke="#1d5a54" stroke-width="1.5"/>
    <path d="M125,6 Q132,-5 142,-5 H215 Q225,-5 232,6 Q225,17 215,17 H142 Q132,17 125,6Z" fill="#1d5a54"/>
  </svg>
  <div class="abs services-label">SERVICES:</div>

  <div class="abs service-item" style="left:41px;top:651px"><svg width="11" height="11"><use href="#tick-soft"/></svg>Bridal Hair and Makeup</div>
  <div class="abs service-item" style="left:41px;top:674px"><svg width="11" height="11"><use href="#tick-soft"/></svg>Bridesmaids and Moms</div>
  <div class="abs service-item" style="left:41px;top:697px"><svg width="11" height="11"><use href="#tick-soft"/></svg>Junior Bridesmaids<br>and Flower Girls</div>
  <div class="abs service-item" style="left:227px;top:651px"><svg width="11" height="11"><use href="#tick-soft"/></svg>Groom's Package</div>
  <div class="abs service-item" style="left:227px;top:674px"><svg width="11" height="11"><use href="#tick-soft"/></svg>Special Occasion Hair<br>and Makeup</div>
  <div class="abs service-item" style="left:227px;top:711px"><svg width="11" height="11"><use href="#tick-soft"/></svg>Proms and Quinceaneras</div>

  <div class="abs gallery-frame"></div>
  <div class="abs gallery">
    <div class="g1" role="img" aria-label="Photo of a blonde bridal updo from behind"></div>
    <div class="g2" role="img" aria-label="Photo of a curled bridal chignon"></div>
    <div class="g3" role="img" aria-label="Photo of a bride holding a small bouquet"></div>
  </div>
  <div class="abs url-bar">www.rovingglowcrew.com</div>
</section>

<section class="rack-card rack-card--back">
  <div class="abs portrait-photo" role="img" aria-label="Close-up photo of a woman having eyeliner applied"></div>
  <svg class="abs back-curve" viewBox="0 0 439 80">
    <path d="M0,18 Q219.5,106 439,18 V80 H0 Z" fill="#8fd3cd"/>
    <path d="M0,28 Q219.5,112 439,28 V80 H0 Z" fill="#1d5a54"/>
  </svg>
  <div class="abs back-band"></div>
  <p class="abs back-lead">Tell us what you envision for your special day<br>and we will customize everything for you! We will<br>give you a perfect, timeless, and flawless look.</p>

  <div class="abs duo-frame duo-a"><div role="img" aria-label="Photo of a stylist finishing an updo with hairspray"></div></div>
  <div class="abs duo-frame duo-b"><div role="img" aria-label="Photo of a stylist placing hair jewelry in an updo"></div></div>

  <p class="abs onsite-note">We can have our team<br>remain at your event for an<br>additional fee to provide<br>touch ups. Trails are not<br>required but, encouraged.<br>For an additional fee we<br>can schedule a trail at<br>your preferred location.</p>

  <div class="abs include-label">WE INCLUDE:</div>
  <div class="abs include-row" style="top:688px"><svg width="11" height="11"><use href="#tick-dark"/></svg>Veil Placement</div>
  <div class="abs include-row" style="top:713px"><svg width="11" height="11"><use href="#tick-dark"/></svg>Skin Prep</div>
  <div class="abs include-row" style="top:738px"><svg width="11" height="11"><use href="#tick-dark"/></svg>Hair Jewelry Placement</div>
  <div class="abs include-row" style="top:765px"><svg width="11" height="11"><use href="#tick-dark"/></svg>False lashes</div>

  <div class="abs fees-box">
    <div class="fees-title">No hidden fees:</div>
    <div class="fee-item"><svg width="11" height="11"><use href="#tick-dark"/></svg>Our cost includes travel up to 25 miles from Harbor Point.</div>
    <div class="fee-item"><svg width="11" height="11"><use href="#tick-dark"/></svg>Travel fees will apply outside of the 25 mile radius.</div>
    <div class="fee-item"><svg width="11" height="11"><use href="#tick-dark"/></svg>Ask about our discounts when also booking our officiant<br>or wedding planner services.</div>
  </div>

  <div class="abs back-footer">www.rovingglowcrew.com</div>
</section>

</body>
</html>
```